Odvetnik - Attorney at law
Sodni tolmač za angleški jezik - English language Court Interpreter
Simple
Marjan Lesk
Odvetnik - Attorney at law Sodni tolmač za angleški jezik - English Language Court Interpreter
Brinjeva ulica 41 6000 Koper Slovenija
info@marjanlesk.example
www.marjanlesk.example
I invite all designers under logo project Attorney Marjan Lesk to participate. Please inform all designers.

```html
<!DOCTYPE html>
<html lang="sl">
<head>
<meta charset="utf-8">
<title>Marjan Lesk – Stationery Set</title>
<link href="https://fonts.googleapis.com/css2?family=Cinzel:wght@500&family=Lato:wght@400;700&display=swap" rel="stylesheet">
<style>
  :root{
    --stage:#3b3b3d;
    --paper:#ffffff;
    --ink:#3f3a7a;
    --accent:#e2652c;
    --muted:#6b6a86;
    --serif:"Cinzel", serif;
    --sans:"Lato", sans-serif;
  }
  *{margin:0;padding:0;box-sizing:border-box}
  html,body{width:1200px;height:684px;overflow:hidden;background:var(--stage)}
  .stage{position:relative;width:1200px;height:684px}

  .brand{display:flex;flex-direction:column;align-items:center;text-align:center}
  .brand-row{display:flex;align-items:center;gap:8px}
  .brand-dot{width:12px;height:12px;border-radius:50%;background:var(--accent)}
  .brand-name{font-family:var(--serif);font-weight:500;color:var(--ink);letter-spacing:.04em;white-space:nowrap}
  .brand-tag{font-family:var(--sans);color:var(--muted);font-size:6px;letter-spacing:.05em;margin-top:2px}

  /* Letterhead */
  .letterhead{position:absolute;left:192px;top:12px;width:408px;height:653px;background:var(--paper)}
  .letterhead .band-top{height:22px;background:var(--ink)}
  .letterhead .brand{position:absolute;top:80px;left:0;right:0}
  .letterhead .brand-name{font-size:22px}
  .letterhead .footer{position:absolute;left:0;right:0;bottom:0;height:34px;background:var(--ink);
    color:#fff;font-family:var(--sans);font-size:5.5px;display:flex;flex-direction:column;align-items:center;justify-content:center;gap:4px}
  .letterhead .footer strong{font-weight:700}

  /* Envelope back */
  .envelope-back{position:absolute;left:643px;top:24px;width:533px;height:264px;background:var(--paper)}
  .envelope-back svg{position:absolute;inset:0}
  .envelope-back .brand{position:absolute;top:112px;left:0;right:0}
  .envelope-back .brand-name{font-size:12px}

  /* Envelope front */
  .envelope-front{position:absolute;left:643px;top:367px;width:533px;height:247px;background:var(--paper)}
  .envelope-front .band-top{height:29px;background:var(--ink);border-bottom:2px solid var(--accent)}
  .envelope-front .brand{position:absolute;top:64px;left:80px;right:0}
  .envelope-front .brand-name{font-size:20px}
  .envelope-front .rule{position:absolute;left:0;right:0;top:201px;height:1.5px;background:var(--accent)}
  .envelope-front .contact{position:absolute;left:16px;right:16px;top:207px;font-family:var(--sans);font-size:5.5px;color:var(--ink);letter-spacing:.02em}

  /* Business card */
  .card{position:absolute;left:91px;top:317px;width:168px;height:108px;background:var(--ink);overflow:hidden}
  .card .role{padding:8px 8px 0;color:#fff;font-family:var(--sans);font-size:4.5px;line-height:1.55;text-align:right}
  .card .role strong{font-size:5px}
  .card .name-band{position:absolute;left:0;right:0;top:42px;height:29px;background:var(--paper);
    display:flex;align-items:center;padding-left:16px}
  .card .brand-name{font-size:14px}
  .card .brand-dot{width:9px;height:9px}
  .card .contact{position:absolute;left:16px;top:76px;color:#fff;font-family:var(--sans);font-size:4.5px;line-height:1.6}
</style>
</head>
<body>
<main class="stage">

  <section class="letterhead" aria-label="Letterhead">
    <div class="band-top"></div>
    <div class="brand">
      <div class="brand-row"><span class="brand-dot"></span><span class="brand-name">Marjan Lesk</span></div>
      <div class="brand-tag">ODVETNIK · ATTORNEY AT LAW</div>
    </div>
    <footer class="footer">
      <span>Brinjeva ulica 41, 6000 Koper, Slovenija &nbsp;|&nbsp; E: info@marjanlesk.example &nbsp;|&nbsp; T: +386 5 630 1127 &nbsp;|&nbsp; F: +386 41 508 334</span>
      <strong>www.marjanlesk.example</strong>
    </footer>
  </section>

  <section class="envelope-back" aria-label="Envelope back">
    <svg width="533" height="264" viewBox="0 0 533 264" fill="none" stroke="#d6d6dc" stroke-width="1.2">
      <polyline points="0,0 266,150 533,0"/>
      <polyline points="0,264 230,130"/>
      <polyline points="533,264 302,130"/>
    </svg>
    <div class="brand">
      <div class="brand-row"><span class="brand-name">Marjan Lesk</span></div>
    </div>
  </section>

  <section class="envelope-front" aria-label="Envelope front">
    <div class="band-top"></div>
    <div class="brand">
      <div class="brand-row"><span class="brand-dot"></span><span class="brand-name">Marjan Lesk</span></div>
      <div class="brand-tag">ODVETNIK · ATTORNEY AT LAW</div>
    </div>
    <div class="rule"></div>
    <p class="contact">Brinjeva ulica 41, 6000 Koper, Slovenija &nbsp;|&nbsp; E: info@marjanlesk.example &nbsp;|&nbsp; T: +386 5 630 1127 &nbsp;|&nbsp; F: +386 41 508 334</p>
  </section>

  <section class="card" aria-label="Business card">
    <p class="role"><strong>Marjan Lesk</strong><br>Odvetnik - Attorney at law<br>Sodni tolmač za angleški jezik - English Language Court Interpreter</p>
    <div class="name-band">
      <div class="brand-row"><span class="brand-dot"></span><span class="brand-name">Marjan Lesk</span></div>
    </div>
    <p class="contact">Brinjeva ulica 41, 6000 Koper, Slovenija<br>info@marjanlesk.example<br>T: +386 5 630 1127 &nbsp; M: +386 41 508 334</p>
  </section>

</main>
</body>
</html>
```